Business Card Design Project

Looking for a simple and stylish business card. We are an Advertising Company. The card Must feature the company logo (attached) and also this info.
p: 0481629054
e: sales@rv-promo.com.au
w: www.rv-promo.com.au
We Advertise mainly using TV screens featured in restaurants and cafe. See website for more about the business.
Not really looking for a plain background, but at the same time do not want to much happening in the Background. I am not really to fussy though with the design or the colour scheme, and I am leaving the creativity part up to you creative designers.

```html
<!DOCTYPE html>
<html lang="en">
<head>
<meta charset="utf-8">
<title>RVPROMO Business Card</title>
<link rel="stylesheet" href="https://fonts.googleapis.com/css2?family=Montserrat:wght@300;400&display=swap">
<style>
  :root {
    --backdrop: #e4e6ea;
    --brand-blue: #1668c0;
    --brand-blue-deep: #0b56a8;
    --brand-blue-light: #2a86d6;
    --brand-pink: #e01f5a;
    --ink: #3a3a3a;
    --paper: #f7f7f7;
    --rule: #2f63c0;
  }
  * { margin: 0; padding: 0; box-sizing: border-box; }
  html, body { width: 1200px; height: 900px; overflow: hidden; }
  body {
    background: var(--backdrop);
    font-family: "Montserrat", Arial, sans-serif;
    display: flex;
    flex-direction: column;
    align-items: center;
    justify-content: center;
    gap: 44px;
  }
  .card {
    position: relative;
    width: 630px;
    height: 360px;
    overflow: hidden;
    box-shadow: 0 6px 18px rgba(0,0,0,0.18);
  }
  .card-front { background: var(--brand-blue); }
  .card-front .waves { position: absolute; inset: 0; width: 100%; height: 100%; }
  .card-front .wordmark {
    position: absolute;
    left: 0; right: 0; top: 50%;
    transform: translateY(-50%);
    text-align: center;
    font-weight: 300;
    font-size: 92px;
    letter-spacing: 6px;
    color: #ffffff;
  }
  .card-back { background: var(--paper); color: var(--ink); }
  .card-back .wordmark {
    position: absolute;
    left: 40px; top: 34px;
    font-weight: 300;
    font-size: 58px;
    letter-spacing: 4px;
    color: var(--brand-blue-deep);
  }
  .contact {
    position: absolute;
    left: 318px; top: 186px;
    width: 312px;
  }
  .contact .person-name { font-size: 25px; font-weight: 400; letter-spacing: 0.5px; }
  .contact .person-role { font-size: 17px; font-weight: 400; margin-top: 2px; }
  .contact .divider { height: 1px; background: var(--rule); margin: 9px 0 12px; }
  .contact .line { display: flex; font-size: 17px; line-height: 22px; }
  .contact .label { width: 26px; color: var(--rule); }
  .contact .web { font-size: 18px; margin-top: 14px; margin-left: -8px; }
  .contact .web .accent-pink { color: var(--brand-pink); }
  .contact .web .accent-blue { color: var(--brand-blue); }
</style>
</head>
<body>
  <section class="card card-front" aria-label="Card front">
    <svg class="waves" viewBox="0 0 630 360" preserveAspectRatio="none" aria-hidden="true">
      <path d="M0 150 C180 90 420 60 630 70 L630 0 L0 0 Z" fill="var(--brand-blue-deep)" opacity="0.55"/>
      <path d="M0 250 C220 170 430 140 630 150 L630 70 C420 60 180 90 0 150 Z" fill="var(--brand-blue-light)" opacity="0.35"/>
      <path d="M0 360 L0 300 C200 240 420 220 630 230 L630 360 Z" fill="var(--brand-blue-deep)" opacity="0.35"/>
    </svg>
    <div class="wordmark">RVPROMO</div>
  </section>

  <section class="card card-back" aria-label="Card back">
    <div class="wordmark">RVPROMO</div>
    <div class="contact">
      <p class="person-name">Dana Whitfield</p>
      <p class="person-role">Operation Manager</p>
      <div class="divider"></div>
      <p class="line"><span class="label">T</span><span>0481629054</span></p>
      <p class="line"><span class="label">E</span><span>sales@rv-promo.com.au</span></p>
      <p class="web">www.<span class="accent-pink">rv</span><span class="accent-blue">-promo</span>.com.au</p>
    </div>
  </section>
</body>
</html>
```